Mox Dune Reel Business cards

Logo, tag line and photo on card
Agent Name
Title
Address
Phone number
Email
Website
Make logo on one side large by rotating  to portrait format.  Keep the background of the logo white.

Contact Information for Business Card
Slogan; Shaping Every Mox Ahead

```html
<!DOCTYPE html>
<html lang="en">
<head>
<meta charset="utf-8">
<title>Mox Dune Reel – Business Cards</title>
<link href="https://fonts.googleapis.com/css2?family=Montserrat:wght@400;500;700;800&display=swap" rel="stylesheet">
<style>
  :root{
    --navy:#0d2766;
    --red:#c30d19;
    --white:#ffffff;
    --stage:#e9e9eb;
    --photo-a:#6b6d72;
    --photo-b:#2b2e34;
    --ghost-navy:#e6e8f0;
    --ghost-red:#f6dede;
  }
  *{margin:0;padding:0;box-sizing:border-box}
  html,body{width:1200px;height:1108px;overflow:hidden}
  body{background:var(--stage);font-family:"Montserrat",sans-serif;position:relative}

  .card{position:absolute;overflow:hidden}
  .card-front{left:230px;top:70px;width:770px;height:440px;background:var(--navy)}
  .card-back{left:213px;top:584px;width:790px;height:451px;background:var(--white)}

  .agent-name{position:absolute;left:38px;top:88px;color:var(--white);font-weight:700;font-size:29px;letter-spacing:.5px;z-index:2}
  .agent-title{position:absolute;left:36px;top:126px;color:var(--white);font-weight:400;font-size:20px;letter-spacing:.6px;z-index:2}

  .contact-list{position:absolute;left:36px;top:190px;list-style:none;z-index:2}
  .contact-list li{display:flex;align-items:center;gap:16px;color:var(--white);font-size:20.5px;height:30px}
  .contact-list svg{width:22px;height:22px;flex:none}

  .address{position:absolute;left:41px;top:290px;color:var(--white);font-size:20.5px;line-height:30px;z-index:2}

  .agent-photo{position:absolute;left:437px;top:14px;width:333px;height:426px;z-index:1;
    background:
      radial-gradient(ellipse 55% 40% at 62% 28%, rgba(150,130,120,.55), transparent 70%),
      linear-gradient(180deg, rgba(13,39,102,0) 0%, var(--photo-a) 45%, var(--photo-b) 100%);}

  .brand-box{position:absolute;left:355px;top:48px;width:140px;height:172px;background:var(--white);padding:4px;z-index:3}
  .brand-box-inner{width:100%;height:100%;border:4px solid var(--red);border-radius:8px;display:flex;flex-direction:column;justify-content:center;align-items:center;color:var(--navy);font-weight:800;font-size:30px;line-height:40px}

  .slogan-band{position:absolute;left:0;top:378px;width:437px;height:62px;background:var(--red);color:var(--white);font-weight:700;font-size:27px;display:flex;align-items:center;padding-left:33px;white-space:nowrap;z-index:2}
  .slogan-fade{position:absolute;left:437px;top:378px;width:120px;height:62px;background:linear-gradient(90deg,rgba(195,13,25,.55),rgba(195,13,25,0));z-index:2}

  .logo-portrait{position:absolute;left:34px;top:78px;width:342px;height:275px;border:7px solid var(--red);border-radius:18px;display:flex;align-items:center;justify-content:center}
  .logo-portrait-name{transform:rotate(90deg);color:var(--navy);font-weight:800;font-size:78px;line-height:84px;text-align:center;white-space:nowrap}

  .logo-ghost{position:absolute;left:412px;top:11px;width:346px;height:430px;border:6px solid var(--ghost-red);border-radius:20px;display:flex;align-items:center;justify-content:center}
  .logo-ghost-name{color:var(--ghost-navy);font-weight:800;font-size:98px;line-height:118px;text-align:center}
</style>
</head>
<body>

<section class="card card-front" aria-label="Business card front">
  <h1 class="agent-name">DANIEL HARLOW</h1>
  <p class="agent-title">MANAGING DIRECTOR</p>

  <ul class="contact-list">
    <li>
      <svg viewBox="0 0 24 24" aria-hidden="true"><path fill="#c30d19" d="M6.6 10.8a15 15 0 0 0 6.6 6.6l2.2-2.2c.3-.3.7-.4 1-.2 1.1.4 2.3.6 3.6.6.6 0 1 .4 1 1V20c0 .6-.4 1-1 1A17 17 0 0 1 3 4c0-.6.4-1 1-1h3.5c.6 0 1 .4 1 1 0 1.3.2 2.5.6 3.6.1.3 0 .7-.2 1z"/></svg>
      044-123 456 789
    </li>
    <li>
      <svg viewBox="0 0 24 24" aria-hidden="true"><rect x="2" y="5" width="20" height="14" fill="#c30d19"/><path d="M2 5l10 8 10-8" fill="none" stroke="#0d2766" stroke-width="1.6"/></svg>
      info@webname.com
    </li>
    <li>
      <svg viewBox="0 0 24 24" aria-hidden="true"><g fill="none" stroke="#c30d19" stroke-width="1.8"><circle cx="12" cy="12" r="9"/><ellipse cx="12" cy="12" rx="4" ry="9"/><path d="M3 12h18M5 7h14M5 17h14"/></g></svg>
      www.websitename.com
    </li>
  </ul>

  <p class="address">421, Address line goes here<br>45452, Country name</p>

  <div class="agent-photo" role="img" aria-label="Portrait photo of the managing director"></div>

  <div class="brand-box">
    <div class="brand-box-inner"><span>Mox</span><span>Dune</span><span>Reel</span></div>
  </div>

  <div class="slogan-band">Shaping Every Mox Ahead</div>
  <div class="slogan-fade" aria-hidden="true"></div>
</section>

<section class="card card-back" aria-label="Business card back">
  <div class="logo-portrait">
    <div class="logo-portrait-name">Mox<br>Dune<br>Reel</div>
  </div>
  <div class="logo-ghost" aria-hidden="true">
    <div class="logo-ghost-name">Mox<br>Dune<br>Reel</div>
  </div>
</section>

</body>
</html>
```